Graphic Design of Business Process

We require an eye-catching, sophisticated design of 2 business processes (attached), that will be used digitally AND for print (to be put on walls in our office).

The basic layout is attached. We require a creative, professional designer to re-design these so that they look appealing but still able to grasp all the information.

We will require vector files and editable project files for final delivery. You may refer to our website (kitefieldmedia.com.au) for an indication of our brand.

If you have any questions, please ask.

Thank you.

```html
<!DOCTYPE html>
<html lang="en">
<head>
<meta charset="utf-8">
<title>Content Hierarchy</title>
<link rel="stylesheet" href="https://fonts.googleapis.com/css2?family=Arimo:wght@400;700&display=swap">
<style>
  :root {
    --page-bg: #ffffff;
    --title-blue: #1670b0;
    --peak-light: #2ea7dc;
    --peak-dark: #2283c0;
    --hero-light: #ec5443;
    --hero-dark: #d2372c;
    --hub-light: #4a914c;
    --hub-dark: #317a3b;
    --hygiene-light: #f48834;
    --hygiene-dark: #e8742a;
    --label-white: #ffffff;
  }
  html, body {
    margin: 0;
    padding: 0;
    overflow: hidden;
    background: var(--page-bg);
  }
  .canvas {
    position: relative;
    width: 1200px;
    height: 750px;
    overflow: hidden;
    background: var(--page-bg);
    font-family: "Arimo", Arial, sans-serif;
  }
  .chart-title {
    position: absolute;
    top: 54px;
    left: 0;
    width: 100%;
    margin: 0;
    text-align: center;
    font-size: 32px;
    font-weight: 700;
    letter-spacing: 0.3px;
    color: var(--title-blue);
  }
  .chart-title span {
    border-bottom: 2px solid var(--title-blue);
    padding-bottom: 1px;
  }
  .pyramid {
    position: absolute;
    top: 0;
    left: 0;
    width: 1200px;
    height: 750px;
  }
  .tier-name {
    font-family: "Arimo", Arial, sans-serif;
    font-weight: 700;
    font-size: 52px;
    fill: var(--label-white);
    text-anchor: middle;
    filter: url(#label-shadow);
  }
  .tier-desc {
    font-family: "Arimo", Arial, sans-serif;
    font-weight: 400;
    font-size: 18px;
    letter-spacing: 0.3px;
    fill: var(--label-white);
    text-anchor: middle;
    filter: url(#label-shadow);
  }
  .base-bracket {
    fill: none;
    stroke: var(--hygiene-dark);
    stroke-width: 6;
    stroke-linecap: round;
    stroke-linejoin: miter;
  }
</style>
</head>
<body>
<div class="canvas">
  <h1 class="chart-title"><span>CONTENT HIERARCHY</span></h1>

  <svg class="pyramid" viewBox="0 0 1440 900" xmlns="http://www.w3.org/2000/svg" aria-label="Content hierarchy pyramid: Hero, Hub and Hygiene">
    <defs>
      <filter id="label-shadow" x="-20%" y="-40%" width="140%" height="180%">
        <feDropShadow dx="1.5" dy="2" stdDeviation="1.5" flood-color="#000" flood-opacity="0.35"/>
      </filter>
    </defs>

    <g class="tier tier-peak">
      <polygon points="718,213 765.3,346 641.1,346" fill="var(--peak-light)"/>
      <polygon points="718,213 794.9,346 765.3,346" fill="var(--peak-dark)"/>
    </g>

    <g class="tier tier-hero">
      <polygon points="641.1,346 765.3,346 812,477 565.4,477" fill="var(--hero-light)"/>
      <polygon points="765.3,346 794.9,346 870.6,477 812,477" fill="var(--hero-dark)"/>
      <text class="tier-name" x="720" y="425">HERO</text>
      <text class="tier-desc" x="720" y="460">TENTPOLE CAMPAIGNS</text>
    </g>

    <g class="tier tier-hub">
      <polygon points="565.4,477 812,477 859,609 489.1,609" fill="var(--hub-light)"/>
      <polygon points="812,477 870.6,477 946.9,609 859,609" fill="var(--hub-dark)"/>
      <text class="tier-name" x="720" y="545">HUB</text>
      <text class="tier-desc" x="720" y="575">REGULAR “PUSH” CONTENT</text>
    </g>

    <g class="tier tier-hygiene">
      <polygon points="489.1,609 859,609 906,741 412.8,741" fill="var(--hygiene-light)"/>
      <polygon points="859,609 946.9,609 1023.2,741 906,741" fill="var(--hygiene-dark)"/>
      <text class="tier-name" x="720" y="683">HYGIENE</text>
      <text class="tier-desc" x="720" y="712">ALWAYS-ON “PULL” CONTENT</text>
    </g>

    <polyline class="base-bracket" points="433,690 399,748 515,748"/>
    <polyline class="base-bracket" points="1003,690 1039,748 922,748"/>
  </svg>
</div>
</body>
</html>
```